Flyer Design Project

We are a storm restoration company that has recently begun restoration from water/flood damage from Hurricane Sandy. We provide disaster relief to homeowners and or commercial property owners after a flood. To start we offer cleanup and remediation which is taking out and disposing of all wet items in a home or business and the cutting out of walls, flooring and other items affected by a flood. We then provide remediation which includes the drying out of a home or business along with a dehumidifier to take all the moisture out of the air and to put it simply dry out the home. We also uses chemicals to clean and provide mold remediation to prevent to growth of mold. We work directly with a customers insurance company if they have flood insurance and after that we provide the services to rebuild and bring their property back to its condition before the storm.

Im looking for an informational type flier that I could insert into our business folders that we give to customers and also to use as fliers to pass out to potential customers. I want potential customers to look at this and feel comfortable with calling my company and working with us.

Company name Bellridge Building Partners. I attached our company logo.

Target Market(s)

Those affected by flooding from Hurricane Sandy

Industry/Entity Type

Insurance

Requirements
Must have
• Company logo, name and colors on flier
Nice to have
• Color photos that have to do with water restoration or showing flood damamge

```html
<!DOCTYPE html>
<html lang="en">
<head>
<meta charset="utf-8">
<title>Bellridge Building Partners – Water Restoration Flyer</title>
<link rel="stylesheet" href="https://fonts.googleapis.com/css2?family=Libre+Franklin:wght@700;800;900&display=swap">
<style>
  :root {
    --navy: #2b3a7c;
    --page: #ffffff;
    --water-top: #cfe9f4;
    --water-mid: #6cc2de;
    --water-low: #7fd0dd;
    --water-base: #48c2cc;
  }
  * { margin: 0; padding: 0; box-sizing: border-box; }
  html, body {
    width: 939px;
    height: 1200px;
    overflow: hidden;
    background: var(--page);
  }
  .flyer {
    position: relative;
    width: 939px;
    height: 1200px;
    background: var(--page);
    font-family: "Libre Franklin", "Franklin Gothic Medium", Arial, sans-serif;
    color: var(--navy);
  }
  .flyer__backdrop {
    position: absolute;
    left: 26px;
    top: 26px;
    width: 887px;
    height: 1148px;
    background:
      radial-gradient(ellipse 60% 35% at 55% 30%, rgba(255,255,255,0.55), rgba(255,255,255,0) 70%),
      linear-gradient(180deg, var(--water-mid) 0%, var(--water-top) 30%, var(--water-low) 58%, var(--water-base) 78%, var(--water-base) 100%);
  }
  .service-call {
    position: absolute;
    right: 87px;
    top: 148px;
    text-align: right;
    font-weight: 800;
    line-height: 1;
  }
  .service-call__hours { font-size: 40px; }
  .service-call__label { font-size: 28px; margin-top: 2px; }
  .service-call__prompt { font-size: 28px; margin-top: 42px; }
  .service-call__phone { font-size: 46px; font-weight: 900; margin-top: 2px; }

  .headline {
    position: absolute;
    left: 106px;
    top: 446px;
    font-size: 36px;
    font-weight: 800;
    line-height: 52px;
    text-transform: uppercase;
  }
  .services {
    position: absolute;
    left: 464px;
    top: 712px;
    width: 390px;
    font-size: 14.4px;
    font-weight: 800;
    line-height: 18.1px;
    text-align: justify;
  }
  .brand {
    position: absolute;
    left: 104px;
    top: 930px;
    width: 310px;
    display: flex;
    align-items: flex-start;
    gap: 16px;
  }
  .brand__square {
    flex: none;
    width: 46px;
    height: 46px;
    background: var(--navy);
    margin-top: 6px;
  }
  .brand__name {
    font-size: 38px;
    font-weight: 800;
    line-height: 44px;
    color: var(--navy);
  }
</style>
</head>
<body>
  <main class="flyer">
    <div class="flyer__backdrop" role="img" aria-label="Close-up photograph of water droplets on glass in blue and teal tones"></div>

    <section class="service-call">
      <p class="service-call__hours">24/7</p>
      <p class="service-call__label">SERVICE</p>
      <p class="service-call__prompt">PLEASE CALL</p>
      <p class="service-call__phone">+1 000 000</p>
    </section>

    <h1 class="headline">Solution for<br>water restoration<br>and<br>flood damage</h1>

    <p class="services">We provide disaster relief to homeowners and or commercial property owners after a flood. To start we offer cleanup and remediation which is taking out and disposing of all wet items in a home or business and the cutting out of walls, flooring and other items affected by a flood. We then provide remediation which includes the drying out of a home or business along with a dehumidifier to take all the moisture out of the air and to put it simply dry out the home. We also uses chemicals to clean and provide mold remediation to prevent to growth of mold. We work directly with a customers insurance company if they have flood insurance and after that we provide the services to rebuild and bring their property back to its condition before the storm.</p>

    <div class="brand">
      <span class="brand__square" aria-hidden="true"></span>
      <p class="brand__name">Bellridge Building Partners</p>
    </div>
  </main>
</body>
</html>
```